Business Card Design Project- Removalist

I would like to surprise my husband to be with a different type of wedding present. His brother (who he owned a removalist business with) suddenly passed away from cancer recently and he has changed his business name to 'TQB' (which stands for Keeping Ted Strong; but the full name doesn't need to be on the business card as it is more of a personal business name). To celebrate the new business I would like to get him some business cards made.
I would like the business name to be listed as 'TQB' and somewhere on the card I would like 'Sydney wide removals and relocation services'. I would like it to be obvious from the front of the card that it is a removalist business card. If a truck or some other feature that makes it look like a removalist business card could added it would be appreciated.
I don't mind what colours are used, but I would like the colour blue to feature somewhere in the design. It can be bright and fun, which is how Ted was.
I will also need the company's email address and phone number listed
The email address is: tqbmoving@brisketmail.example
The contact number is: 0418 902 364
I don't need a contact name listed on the card, but perhaps 'Owned and operated by the Pemberton family' could be added near the contact details in small font.
Thank you very much for considering this project!
Kind regards,
Fiona
Updates
Could you please change the mobile contact number to 0418 902 364. This is the only contact phone number required on the card now.
Thank you!
Industry/Entity Type
Wedding
Look and feel
Each slider illustrates characteristics of the customer's brand and the style your logo design should communicate.

```html
<!DOCTYPE html>
<html lang="en">
<head>
<meta charset="utf-8">
<title>TQB Business Cards</title>
<link rel="stylesheet" href="https://fonts.googleapis.com/css2?family=Questrial&family=Montserrat:wght@600&display=swap">
<style>
  :root {
    --backdrop: #1c1c1c;
    --card-white: #ffffff;
    --brand-blue: #1f4f98;
    --brand-blue-deep: #233d84;
    --brand-blue-bright: #0f6db3;
    --ink-blue: #175d93;
    --ink-grey: #555a60;
    --rule: #555555;
    --photo-light: #e6d3b8;
    --photo-mid: #c69a6c;
    --photo-dark: #8a6a4e;
  }
  * { box-sizing: border-box; margin: 0; padding: 0; }
  html, body {
    width: 1200px; height: 722px; overflow: hidden;
    background: var(--backdrop);
  }
  .sheet { position: relative; width: 1200px; height: 722px; }
  .card {
    position: absolute; width: 515px; height: 294px;
    border-radius: 12px; overflow: hidden;
    box-shadow: 0 4px 14px rgba(0,0,0,.55);
  }
  .card--front { left: 75px; top: 51px; background: var(--card-white); }
  .card--photo {
    left: 610px; top: 54px;
    background: linear-gradient(120deg, var(--photo-mid) 0%, var(--photo-light) 45%, var(--photo-light) 55%, var(--photo-dark) 100%);
  }
  .card--back {
    left: 375px; top: 375px;
    background: linear-gradient(90deg, var(--brand-blue-deep) 0%, var(--brand-blue) 50%, var(--brand-blue-bright) 100%);
  }
  .wordmark {
    font-family: "Montserrat", sans-serif; font-weight: 600;
    letter-spacing: 2px; line-height: 1;
  }
  .front__logo {
    position: absolute; left: 0; right: 0; top: 72px;
    text-align: center; font-size: 76px; color: var(--brand-blue);
  }
  .front__tagline {
    position: absolute; left: 0; right: 0; top: 160px;
    text-align: center; font-family: "Questrial", sans-serif;
    font-size: 10.5px; color: var(--ink-grey);
  }
  .front__rule {
    position: absolute; left: 0; right: 0; top: 213px;
    height: 2px; background: var(--rule);
  }
  .front__owners {
    position: absolute; left: 0; right: 0; top: 230px;
    text-align: center; font-family: "Questrial", sans-serif;
    font-size: 20.5px; color: var(--ink-blue);
  }
  .front__contacts {
    position: absolute; left: 0; right: 0; top: 260px;
    display: flex; justify-content: center; gap: 16px;
    font-family: "Questrial", sans-serif; font-size: 13px; color: var(--ink-grey);
  }
  .contact { display: flex; align-items: center; gap: 5px; }
  .contact svg { width: 11px; height: 11px; fill: var(--ink-grey); }
  .photo__logo {
    position: absolute; right: 22px; top: 122px;
    font-size: 48px; color: #ffffff;
  }
  .back__logo {
    position: absolute; left: 0; right: 0; top: 110px;
    text-align: center; font-size: 62px; color: #ffffff;
  }
</style>
</head>
<body>
<main class="sheet">
  <section class="card card--front">
    <div class="front__logo wordmark">TQB</div>
    <div class="front__tagline">Sydney Wide Removals &amp; Relocation Services</div>
    <div class="front__rule"></div>
    <div class="front__owners">Owned and operated by the Pemberton family</div>
    <div class="front__contacts">
      <span class="contact">
        <svg viewBox="0 0 24 24" aria-hidden="true"><path d="M6.6 10.8a15.1 15.1 0 0 0 6.6 6.6l2.2-2.2a1 1 0 0 1 1-.25 11.4 11.4 0 0 0 3.6.57 1 1 0 0 1 1 1V20a1 1 0 0 1-1 1A17 17 0 0 1 3 4a1 1 0 0 1 1-1h3.5a1 1 0 0 1 1 1c0 1.25.2 2.45.57 3.57a1 1 0 0 1-.25 1z"/></svg>
        0418 902 364
      </span>
      <span class="contact">
        <svg viewBox="0 0 24 24" aria-hidden="true"><path d="M2 6h20v12H2z M2 6l10 7 10-7" fill="none" stroke="#555a60" stroke-width="2.4"/></svg>
        tqbmoving@brisketmail.example
      </span>
    </div>
  </section>

  <section class="card card--photo" role="img" aria-label="Photo of a smiling couple sitting among moving boxes with glasses of wine">
    <div class="photo__logo wordmark">TQB</div>
  </section>

  <section class="card card--back">
    <div class="back__logo wordmark">TQB</div>
  </section>
</main>
</body>
</html>
```